Webdesign für Entrümpelungsfirma
Zielgruppe
Unsere Firma heißt Tolvo Hausservice und wir bieten folgende Dienstleistungen an:
Haushaltsauflösungen, Entrümpelungen, Messie-Wohnungen, Demontage-Arbeiten, Gartenpflege.
Aufgabenstellung
Unsere jetzige Seite: www.hausdienst-brenfeld.de
Das Logo bleibt bestehen. Es wäre schön, wenn das neue Design die Farben aufnehmen würde. Es geht erstmal nur um die Startseite.
Die Struktur soll klar und übersichtlich sein.
Wir möchten Vertrauen erwecken, aber nicht langweilig wirken. Das Design soll pfiffig sein und den Kunden aufmerksam machen.
Eine Seite, die uns sehr gut gefällt:
http://www.kramkurt.de/

```html
<!DOCTYPE html>
<html lang="de">
<head>
<meta charset="utf-8">
<title>Tolvo Hausservice – Startseite</title>
<link href="https://fonts.googleapis.com/css2?family=Yanone+Kaffeesatz:wght@500;700&family=Lato:wght@400;700&display=swap" rel="stylesheet">
<style>
:root{
  --blue:#00adef;
  --yellow:#f3cb00;
  --green:#8a9c00;
  --navy:#0b4ea2;
  --navy-dark:#0047a0;
  --orange:#f26522;
  --light:#f2f2f2;
  --light2:#e9e9e9;
  --heading:'Yanone Kaffeesatz',sans-serif;
  --body:'Lato',sans-serif;
}
*{box-sizing:border-box;margin:0;padding:0}
html,body{width:1200px;height:3582px;overflow:hidden;background:#fff;font-family:var(--body)}
.page{position:relative;width:1200px;height:3582px}

/* Header */
.header{position:absolute;top:0;left:0;width:1200px;height:113px;background:#fff}
.brand{position:absolute;left:222px;top:34px;display:flex;align-items:center;gap:16px}
.brand-dot{width:56px;height:56px;border-radius:50%;background:var(--yellow)}
.brand-name{font-family:var(--heading);font-weight:700;font-size:32px;color:var(--navy);letter-spacing:.3px}
.meta-links{position:absolute;right:234px;top:14px;font-size:11px;color:var(--navy)}
.meta-links span{margin:0 5px}
.hotline{position:absolute;right:232px;top:66px;display:flex;align-items:center;gap:10px;font-family:var(--heading);font-weight:700;font-size:40px;color:var(--navy);line-height:1}
.hotline svg{width:26px;height:26px}

.nav{position:absolute;top:113px;left:0;width:1200px;height:32px;background:var(--navy)}
.nav-item{position:absolute;top:9px;font-size:11.5px;color:#fff;text-transform:uppercase;letter-spacing:.2px;display:flex;align-items:center;gap:8px}
.nav-item::after{content:"";border:4px solid transparent;border-top-color:#fff;border-bottom:0;width:0;height:0}

/* Service bands */
.service{position:absolute;left:0;width:1200px;background:#fff;overflow:hidden}
.panel{position:absolute;inset:0}
.photo{position:absolute;border-radius:6px}
.copy{position:absolute;top:0;bottom:0;display:flex;flex-direction:column;justify-content:center;gap:33px}
.copy--left{left:232px;align-items:flex-start}
.copy--right{right:234px;align-items:flex-end;text-align:right}
.service-title{font-family:var(--heading);font-weight:700;font-size:42px;line-height:45px;color:#fff;text-transform:uppercase;letter-spacing:.2px}
.btn{display:inline-block;width:107px;height:31px;line-height:31px;text-align:center;background:var(--navy-dark);color:#fff;font-size:11px;font-weight:700}

.blue{background:var(--blue)}
.yellow{background:var(--yellow)}
.green{background:var(--green)}

/* Testimonials */
.reviews{position:absolute;top:2727px;left:0;width:1200px;height:377px;background:var(--light)}
.section-title{font-family:var(--heading);font-weight:700;font-size:38px;color:var(--navy);text-transform:uppercase;text-align:center;line-height:46px}
.reviews .section-title{position:absolute;top:54px;width:100%}
.quote-mark{position:absolute;left:290px;top:96px;font-family:Georgia,serif;font-size:130px;line-height:1;color:#d3dae8}
.quote{position:absolute;left:290px;top:146px;width:620px;text-align:center;font-size:14px;line-height:23px;color:var(--navy)}
.quote p{margin-bottom:22px}
.arrow{position:absolute;top:220px;width:38px;height:38px;border-radius:50%;background:var(--navy-dark);display:flex;align-items:center;justify-content:center}
.arrow svg{width:12px;height:12px}

/* Contact */
.contact{position:absolute;top:3104px;left:0;width:1200px;height:445px;background:var(--light2)}
.contact .section-title{position:absolute;top:40px;width:100%}
.field{position:absolute;background:#fff;border-radius:3px;font-size:10.5px;color:var(--navy);text-transform:uppercase;padding:10px 12px}
.send{position:absolute;left:359px;top:376px;width:107px;height:31px;line-height:31px;background:var(--navy-dark);color:#fff;font-size:11px;font-weight:700;text-align:center}
.address{position:absolute;left:673px;top:168px;font-size:14px;line-height:22.5px;color:var(--navy)}
.address .gap{height:23px}
.address .row{display:flex;align-items:center;gap:8px}
.address svg{width:13px;height:13px}

.footer-bar{position:absolute;top:3549px;left:0;width:1200px;height:33px;background:var(--orange);color:#fff;font-size:14.5px;font-weight:700;display:flex;align-items:center;justify-content:center;gap:5px}
.footer-bar svg{width:13px;height:13px}
</style>
</head>
<body>
<div class="page">

  <header class="header">
    <div class="brand"><span class="brand-dot"></span><span class="brand-name">Tolvo Hausservice</span></div>
    <div class="meta-links">Unser Team<span>|</span>Kontakt<span>|</span>Impressum<span>|</span>Preise</div>
    <div class="hotline">
      <svg viewBox="0 0 24 24"><path fill="#0b4ea2" d="M6.6 10.8c1.4 2.8 3.8 5.1 6.6 6.6l2.2-2.2c.3-.3.7-.4 1-.2 1.1.4 2.3.6 3.6.6.6 0 1 .4 1 1V20c0 .6-.4 1-1 1C10.6 21 3 13.4 3 4c0-.6.4-1 1-1h3.5c.6 0 1 .4 1 1 0 1.3.2 2.5.6 3.6.1.3 0 .7-.2 1L6.6 10.8z"/></svg>
      07431 5527180
    </div>
  </header>

  <nav class="nav">
    <span class="nav-item" style="left:232px">Haushaltsauflösungen &amp; Entrümpelungen</span>
    <span class="nav-item" style="left:552px">Messie-Wohnung</span>
    <span class="nav-item" style="left:712px">Gartenpflege</span>
    <span class="nav-item" style="left:852px">Möbel-Montage</span>
  </nav>

  <!-- Haushaltsauflösungen -->
  <section class="service" style="top:145px;height:374px">
    <div class="panel blue" style="clip-path:polygon(0 0,672px 0,530px 100%,0 100%)"></div>
    <div class="photo" role="img" aria-label="Umzugskarton voller Hausrat und Sportgeräte" style="left:690px;top:40px;width:390px;height:334px;background:linear-gradient(160deg,#f4f4f4,#e2cfae 65%,#c9a97a)"></div>
    <div class="copy copy--left"><h2 class="service-title">Haushaltsauflösungen &amp;<br>Entrümpelungen</h2><span class="btn">anzeigen</span></div>
  </section>

  <!-- Messie-Wohnungen -->
  <section class="service" style="top:519px;height:375px">
    <div class="panel yellow" style="clip-path:polygon(530px 0,100% 0,100% 100%,672px 100%)"></div>
    <div class="photo" role="img" aria-label="Ledersofa mit aufgetürmtem Gerümpel" style="left:60px;top:45px;width:520px;height:310px;background:linear-gradient(160deg,#f6f6f6,#d9b08a 55%,#b8643c)"></div>
    <div class="copy copy--right"><h2 class="service-title">Messie-Wohnungen</h2><span class="btn">anzeigen</span></div>
  </section>

  <!-- Gartenpflege -->
  <section class="service" style="top:894px;height:356px">
    <div class="panel green" style="clip-path:polygon(0 0,672px 0,537px 100%,0 100%)"></div>
    <div class="photo" role="img" aria-label="Zwei Gärtner mit Hüten, Schürzen und Gartenwerkzeug" style="left:630px;top:20px;width:430px;height:336px;background:linear-gradient(170deg,#f6f6f6,#e8d48a 45%,#4f9a5a)"></div>
    <div class="copy copy--left"><h2 class="service-title">Gartenpflege</h2><span class="btn">anzeigen</span></div>
  </section>

  <!-- Möbel-Montage -->
  <section class="service" style="top:1250px;height:376px">
    <div class="panel blue" style="clip-path:polygon(540px 0,100% 0,100% 100%,680px 100%)"></div>
    <div class="photo" role="img" aria-label="Handwerker in Latzhose mit Akkuschrauber" style="left:220px;top:30px;width:290px;height:346px;background:linear-gradient(170deg,#f6f6f6,#e6e6e6 45%,#3f63c0)"></div>
    <div class="copy copy--right"><h2 class="service-title">Möbel-Montage</h2><span class="btn">anzeigen</span></div>
  </section>

  <!-- Allround-Service -->
  <section class="service" style="top:1626px;height:356px">
    <div class="panel yellow" style="clip-path:polygon(0 0,680px 0,542px 100%,0 100%)"></div>
    <div class="photo" role="img" aria-label="Entspannter Geschäftsmann im Liegestuhl" style="left:670px;top:35px;width:400px;height:321px;background:linear-gradient(170deg,#f6f6f6,#c9c4bd 50%,#7a6e64)"></div>
    <div class="copy copy--left"><h2 class="service-title">Allround-Service</h2><span class="btn">anzeigen</span></div>
  </section>

  <!-- Wertanrechnung -->
  <section class="service" style="top:1982px;height:372px">
    <div class="panel green" style="clip-path:polygon(545px 0,100% 0,100% 100%,686px 100%)"></div>
    <div class="photo" role="img" aria-label="Vergoldeter antiker Konsolentisch" style="left:215px;top:50px;width:280px;height:285px;background:linear-gradient(170deg,#f6f2e4,#d6ae55 55%,#a7782b)"></div>
    <div class="copy copy--right"><h2 class="service-title">Wertanrechnung-<br>Ihr Vorteil</h2><span class="btn">anzeigen</span></div>
  </section>

  <!-- Unser Team -->
  <section class="service" style="top:2354px;height:373px">
    <div class="panel blue" style="clip-path:polygon(0 0,686px 0,542px 100%,0 100%)"></div>
    <div class="photo" role="img" aria-label="Team aus fünf Personen in weißen T-Shirts" style="left:620px;top:45px;width:500px;height:328px;background:linear-gradient(170deg,#f6f6f6,#ececec 50%,#6f86a8)"></div>
    <div class="copy copy--left"><h2 class="service-title">Unser Team</h2><span class="btn">anzeigen</span></div>
  </section>

  <!-- Kundenmeinungen -->
  <section class="reviews">
    <h2 class="section-title">Meinungen unserer Kunden</h2>
    <div class="quote-mark">“</div>
    <div class="quote">
      <p>Bei der Auflösung meiner Zweitwohnung in Haldenau habe ich die Firma TOLVO Hausservice beauftragt. Der Termin kam sehr kurzfristig zu Stande, die Arbeit wurde aufs Beste erledigt und auf kurzfristige Wünsche (z.B. mehr Möbel zur Entsorgung als geplant) wurde schnell und zuvorkommend eingegangen.</p>
      <p>Kurz: Auftrag klasse erledigt, jederzeit gerne wieder!</p>
      <p>M. Reinhold / Kassel</p>
    </div>
    <span class="arrow" style="left:232px"><svg viewBox="0 0 12 12"><path d="M8 1 3 6l5 5" stroke="#fff" stroke-width="2" fill="none"/></svg></span>
    <span class="arrow" style="left:929px"><svg viewBox="0 0 12 12"><path d="M4 1l5 5-5 5" stroke="#fff" stroke-width="2" fill="none"/></svg></span>
  </section>

  <!-- Kontakt -->
  <section class="contact">
    <h2 class="section-title">Tolvo Hausservice: Ihr starker Partner rund um’s Haus<br>Kontaktieren Sie uns!</h2>
    <div class="field" style="left:232px;top:164px;width:170px;height:31px">Name*</div>
    <div class="field" style="left:420px;top:164px;width:170px;height:31px">E-Mail*</div>
    <div class="field" style="left:232px;top:208px;width:358px;height:31px">Betreff</div>
    <div class="field" style="left:232px;top:251px;width:358px;height:106px">Ihre Nachricht</div>
    <div class="send">absenden</div>
    <div class="address">
      <div>Wendland GmbH</div>
      <div>Lindenstieg 7/2</div>
      <div>79613 Brenfeld-Au</div>
      <div class="gap"></div>
      <div class="row"><svg viewBox="0 0 24 24"><path fill="#0b4ea2" d="M6.6 10.8c1.4 2.8 3.8 5.1 6.6 6.6l2.2-2.2c.3-.3.7-.4 1-.2 1.1.4 2.3.6 3.6.6.6 0 1 .4 1 1V20c0 .6-.4 1-1 1C10.6 21 3 13.4 3 4c0-.6.4-1 1-1h3.5c.6 0 1 .4 1 1 0 1.3.2 2.5.6 3.6.1.3 0 .7-.2 1L6.6 10.8z"/></svg>07431 5527180</div>
      <div class="row"><svg viewBox="0 0 24 24"><rect x="3" y="8" width="18" height="13" rx="2" fill="#0b4ea2"/><rect x="7" y="3" width="10" height="7" fill="#0b4ea2"/><rect x="9" y="12" width="6" height="2" fill="#fff"/><rect x="9" y="16" width="6" height="2" fill="#fff"/></svg>07431 552 7189</div>
    </div>
  </section>

  <div class="footer-bar">Fordern Sie ein kostenloses Angebot unter
    <svg viewBox="0 0 24 24"><path fill="#fff" d="M6.6 10.8c1.4 2.8 3.8 5.1 6.6 6.6l2.2-2.2c.3-.3.7-.4 1-.2 1.1.4 2.3.6 3.6.6.6 0 1 .4 1 1V20c0 .6-.4 1-1 1C10.6 21 3 13.4 3 4c0-.6.4-1 1-1h3.5c.6 0 1 .4 1 1 0 1.3.2 2.5.6 3.6.1.3 0 .7-.2 1L6.6 10.8z"/></svg>
    07431 5527180</div>

</div>
</body>
</html>
```